Very Simple Web Redesign Project - Using Photoshop

Required is a very simple website home page redesign for the following site: http://www.kestrelslateworks.com.au/
I require this as a Photoshop design.
The basic look and feel of the site needs to remain.
Specifically the colours don't need to be changed.
The positioning of the site is currently correct for the target market.
The site does not need to be made super slick looking. Just upgraded to a new version.
The current text can all be used.
The only menus necessary are a horizontal menu at the top, and a simple horizontal text menu at the bottom of the page. Do NOT retain the vertical menu on the home page (having the items "Our Gallery", "Our Services", "Enquire Now").
Give the horizontal menu the following items:
Home | Slate Roof Repairs | Slate Reroofing | Slate Roof Benefits | Other Services | Photo Gallery | FAQ's | Free Quote | Contact Us
The picture of the house at the top RHS of the page needs to be reduced in size by approx 50% and moved to the top LHS of the page.
Please place the following text into the top of the page:
"Call Now: 0427 618 302"
Keep the four pictures on the home page layout. Some larger images attached.
Thanks,
Ned
Updates
Hi,
Thanks for all the designs.
I am working with my client to get which one they like the most.
Thanks,
Ned

```html
<!DOCTYPE html>
<html lang="en">
<head>
<meta charset="utf-8">
<title>Kestrel Slate Works</title>
<link href="https://fonts.googleapis.com/css2?family=Arimo:wght@400;700&display=swap" rel="stylesheet">
<style>
:root{
  --green-bright:#4ea60c;
  --green-header:#3f8d17;
  --green-footer:#388a0a;
  --green-footer-box:#2d5e14;
  --green-button:#3f8a1c;
  --dark-side:#323431;
  --panel:#c5c5d0;
  --sidebar:#e8e8ea;
  --card:#f4f4f8;
  --ink:#111;
  --white:#fff;
  --call:#ffff33;
  --logo:#cfe3f7;
  --footer-link:#d8e8c8;
}
*{margin:0;padding:0;box-sizing:border-box}
html,body{width:1200px;height:1113px;overflow:hidden}
body{position:relative;font-family:"Arimo",Arial,sans-serif;background:var(--dark-side);color:var(--ink)}
.top-bar{position:absolute;left:0;top:0;width:1200px;height:48px;background:var(--green-bright);z-index:2}
.date{position:absolute;left:26px;top:20px;font-size:15px;letter-spacing:.4px;color:#1a2a10}
.call{position:absolute;left:746px;top:15px;display:flex;align-items:center;gap:12px}
.call-text{font-weight:700;font-size:21px;color:var(--call)}
.header{position:absolute;left:0;top:48px;width:1200px;height:183px;background:linear-gradient(180deg,#3f8d17,#3b8617);z-index:1}
.house{position:absolute;left:32px;top:44px;width:88px;height:91px;background:linear-gradient(160deg,#c8d84a,#6aa82a);border-radius:4px}
.brand{position:absolute;left:145px;top:66px;font-size:52px;font-weight:700;color:var(--logo);white-space:nowrap}
.strip{position:absolute;left:0;top:231px;width:1200px;height:62px;background:var(--green-bright)}
.nav{position:absolute;left:0;top:250px;width:1200px;height:29px;border-top:1px solid var(--white);border-bottom:1px solid var(--white);display:flex;justify-content:center;align-items:center}
.nav a{color:var(--white);text-decoration:none;font-size:16px;padding:0 8px;line-height:27px;border-left:1px solid var(--white);white-space:nowrap}
.nav a:first-child{border-left:none}
.main{position:absolute;left:46px;top:293px;width:1108px;height:670px;background:var(--panel)}
.sidebar{position:absolute;left:75px;top:321px;width:278px;height:596px;background:var(--sidebar);border-radius:8px}
.area{position:absolute;left:88px;top:334px;width:253px;height:252px;background:var(--card);border-radius:8px;padding:50px 18px 0 18px;font-size:15px;line-height:19.5px;letter-spacing:.3px;hyphens:auto}
.photo{position:absolute;left:409px;top:321px;width:668px;height:287px;background:linear-gradient(180deg,#9cb8d8 0%,#6d7480 45%,#4d6a3a 100%)}
.dots{position:absolute;left:636px;top:619px;display:flex;gap:5px}
.dot{width:24px;height:24px;border-radius:50%;background:var(--green-button)}
.dot.active{border:2px solid #cfe3b8}
.content{position:absolute;left:368px;top:650px;width:766px;height:267px;background:var(--card);border-radius:8px;padding:18px 44px 18px 14px;font-size:15px;line-height:20px;letter-spacing:.3px}
.content p+p{margin-top:19px}
.footer{position:absolute;left:0;top:963px;width:1200px;height:150px;background:var(--green-footer)}
.footer-box{position:absolute;left:75px;top:978px;width:1062px;height:115px;background:var(--green-footer-box);border-radius:8px}
.footer-links{position:absolute;left:0;top:1021px;width:1200px;text-align:center;font-size:14px;color:var(--footer-link);white-space:nowrap}
.copyright{position:absolute;left:0;top:1052px;width:1200px;text-align:center;font-size:13px;font-weight:700;color:var(--white)}
</style>
</head>
<body>
<div class="top-bar">
  <div class="date">Monday, November 14, 2011 03:41 PM</div>
  <div class="call">
    <svg width="47" height="48" viewBox="0 0 47 48" aria-hidden="true">
      <rect x="1" y="1" width="45" height="46" rx="7" fill="#1b6fb8" stroke="#0d3f70"/>
      <rect x="5" y="5" width="37" height="38" rx="5" fill="#fff"/>
      <path d="M14 11c3-2 5 0 6 3l1 4c0 2-2 3-3 4 1 4 4 7 8 9 1-1 2-3 4-3l4 1c3 1 5 3 3 6-2 3-5 4-9 3-9-3-15-10-17-19-1-4 0-6 3-8z" fill="#1b6fb8"/>
    </svg>
    <span class="call-text">Call Now: 0427 618 302</span>
  </div>
</div>
<header class="header">
  <div class="house" role="img" aria-label="Illustration of a green-roofed house"></div>
  <div class="brand">Kestrel Slate Works</div>
</header>
<div class="strip"></div>
<nav class="nav">
  <a href="#">Home</a><a href="#">Slate Roof Repairs</a><a href="#">Slate Reroofing</a><a href="#">Slate Roof Benefits</a><a href="#">Other Services</a><a href="#">Photo Gallery</a><a href="#">FAQ's</a><a href="#">Free Quote</a><a href="#">Contact Us</a>
</nav>
<main class="main"></main>
<aside class="sidebar"></aside>
<div class="area" lang="en">We service all inner city suburbs of Sydney roughly covering an area encompassing Gordon to Epping, Mosman to Bondi, Coogee to Kogarah and Kingsgrove to Burwood and Concord</div>
<div class="photo" role="img" aria-label="Photo of a slate roof on a house with trees and blue sky"></div>
<div class="dots"><span class="dot active"></span><span class="dot"></span><span class="dot"></span><span class="dot"></span><span class="dot"></span></div>
<section class="content">
  <p>At Kestrel Slate Works we specialize in the upkeep, maintenance, repair and replacement of all types of slate roof as well as wood shingles. We can track down the leak that just won't go away or give your house a complete re-roof. We can also provide all your guttering needs.</p>
  <p>Kestrel Slate Works is a small company and as such we do not have the overheads that larger companies do. Quality work and attention to detail are our trademark.</p>
  <p>All photos on this website consist of work which I have personally done. The above photos provide at a quick glance a reasonable cross section of the type of work I do.</p>
  <p>By clicking on the Photo Gallery link you can see other work including some before and after shots.</p>
</section>
<footer class="footer"></footer>
<div class="footer-box"></div>
<div class="footer-links">Home &nbsp; Slate Roof Repairs | Slate Reroofing | Slate Roof Benefits | Other Services | Photo Gallery | FAQ's | Free Quote | Contact Us</div>
<div class="copyright">© 2009 Kestrel Slate Works</div>
</body>
</html>
```